Brightwave Business Card

Professional Business Card Design required using the attached contact information.

Contact information can be rearranged as required.

The company is a new start up venture developing solar systems, the branding should be in keeping with that of one of the investors whose website is as follows https://www.quorvex.com/

```html
<!DOCTYPE html>
<html lang="en">
<head>
<meta charset="utf-8">
<title>Brightwave Solar – Business Card</title>
<link href="https://fonts.googleapis.com/css2?family=Open+Sans:wght@400;600;700&display=swap" rel="stylesheet">
<style>
  :root {
    --card-light: #f4f3ef;
    --card-mid: #e8e6e0;
    --green-deep: #1f8a63;
    --green-mid: #3a9c77;
    --green-pale: #a9d2c0;
    --band-tint: rgba(150, 205, 180, 0.45);
    --ink: #222222;
    --name-green: #0f3b2c;
    --icon: #ffffff;
  }
  * { margin: 0; padding: 0; box-sizing: border-box; }
  html, body {
    width: 1200px;
    height: 622px;
    overflow: hidden;
    background: var(--card-light);
  }
  .business-card {
    position: relative;
    width: 1200px;
    height: 622px;
    overflow: hidden;
    font-family: "Open Sans", Arial, sans-serif;
    background: linear-gradient(180deg, var(--card-light) 0%, var(--card-mid) 100%);
  }
  .card-shapes {
    position: absolute;
    inset: 0;
    width: 1200px;
    height: 622px;
  }
  .company-name {
    position: absolute;
    left: 120px;
    top: 96px;
    font-size: 40px;
    font-weight: 700;
    color: var(--name-green);
    white-space: nowrap;
  }
  .company-dot {
    position: absolute;
    left: 92px;
    top: 117px;
    width: 16px;
    height: 16px;
    border-radius: 50%;
    background: var(--green-deep);
  }
  .person-name {
    position: absolute;
    right: 40px;
    top: 250px;
    font-size: 42px;
    font-weight: 700;
    color: var(--name-green);
    letter-spacing: 0.5px;
    white-space: nowrap;
  }
  .contact-line {
    position: absolute;
    color: var(--ink);
    white-space: nowrap;
  }
  .contact-phone { left: 150px; top: 422px; font-size: 20px; }
  .contact-email { left: 150px; top: 474px; font-size: 20px; }
  .contact-address { left: 150px; top: 524px; font-size: 17px; line-height: 25px; }
  .contact-icon {
    position: absolute;
    left: 98px;
    width: 24px;
    height: 24px;
  }
  .icon-phone { top: 424px; }
  .icon-mail { top: 476px; }
  .icon-pin { top: 536px; }
</style>
</head>
<body>
<main class="business-card">
  <svg class="card-shapes" viewBox="0 0 1200 622" aria-hidden="true">
    <rect class="side-column" x="0" y="0" width="40" height="622" fill="var(--green-deep)"/>
    <rect class="side-rule" x="52" y="0" width="6" height="622" fill="var(--green-pale)"/>
    <rect class="icon-strip" x="84" y="410" width="52" height="170" fill="var(--green-mid)"/>
    <rect class="band-phone" x="136" y="410" width="560" height="46" fill="var(--band-tint)"/>
    <rect class="band-email" x="136" y="462" width="560" height="46" fill="var(--band-tint)"/>
    <rect class="band-address" x="136" y="514" width="560" height="66" fill="var(--band-tint)"/>
    <rect class="name-rule" x="760" y="318" width="400" height="5" fill="var(--green-deep)"/>
    <polygon class="corner-block" points="1200,360 1200,622 820,622" fill="var(--green-deep)"/>
    <polygon class="corner-tint" points="1200,300 1200,360 900,622 780,622" fill="var(--green-pale)" opacity="0.7"/>
  </svg>

  <span class="company-dot" aria-hidden="true"></span>
  <div class="company-name">Brightwave Solar</div>

  <h1 class="person-name">DANIEL CORROW</h1>

  <svg class="contact-icon icon-phone" viewBox="0 0 24 24" aria-hidden="true">
    <path d="M3 8c0-2 3-4 9-4s9 2 9 4v2h-5V8H8v2H3z M6 11h12l2 9H4z" fill="var(--icon)"/>
    <circle cx="12" cy="15.5" r="2.5" fill="var(--green-mid)"/>
  </svg>
  <p class="contact-line contact-phone">Direct: +1 (617) 555-0142</p>

  <svg class="contact-icon icon-mail" viewBox="0 0 24 24" aria-hidden="true">
    <rect x="2" y="5" width="20" height="14" fill="var(--icon)"/>
    <polyline points="2,5 12,13 22,5" fill="none" stroke="var(--green-mid)" stroke-width="1.6"/>
  </svg>
  <p class="contact-line contact-email">daniel.corrow@brightwavesolar.com</p>

  <svg class="contact-icon icon-pin" viewBox="0 0 24 24" aria-hidden="true">
    <path d="M12 2a7 7 0 0 0-7 7c0 5 7 13 7 13s7-8 7-13a7 7 0 0 0-7-7z" fill="var(--icon)"/>
    <circle cx="12" cy="9" r="2.6" fill="var(--green-mid)"/>
  </svg>
  <p class="contact-line contact-address">Brightwave Solar LLC<br>318 Harbor Street, Boston, MA 02110</p>
</main>
</body>
</html>
```